Our 2023 Comprehensive Needs Assessment needs a cover. We take data and produce an indepth beautiful report for our clients. Attached is the color palette we are going with. Let me know if you need me to send any additional information. This cover will be printed as well as used digitally.

```html
<!DOCTYPE html>
<html lang="en">
<head>
<meta charset="utf-8">
<title>2023 Comprehensive Needs Assessment – Fairmere School District</title>
<link rel="stylesheet" href="https://fonts.googleapis.com/css2?family=Archivo+Black&family=Bebas+Neue&family=Arimo:wght@400&display=swap">
<style>
  :root {
    --bg: #c9cacc;
    --paper: #ffffff;
    --navy: #252f47;
    --teal: #1d4a66;
    --spine-top: #1f4c6b;
    --spine-bottom: #14243a;
    --green: #7ab648;
    --magenta: #a8336b;
    --yellow: #ffc20e;
    --orange: #f39a21;
    --ink: #1c1c1c;
  }
  * { margin: 0; padding: 0; box-sizing: border-box; }
  html, body { width: 1200px; height: 972px; overflow: hidden; background: var(--bg); }
  .wrap {
    position: absolute; left: 145px; top: 106px;
    width: 910px; height: 760px; display: flex;
    box-shadow: 0 10px 30px rgba(0,0,0,.18);
  }

  /* Back cover */
  .back { position: relative; width: 430px; height: 760px; background: var(--paper); padding: 30px 30px 0; }
  .back-kicker { font-family: "Bebas Neue", sans-serif; font-weight: 400; color: var(--teal); font-size: 31px; line-height: 1; text-align: center; white-space: nowrap; }
  .back-district { font-family: "Archivo Black", sans-serif; font-weight: 400; color: var(--navy); font-size: 44px; line-height: 1.1; text-align: center; letter-spacing: 1px; }
  .back-district-sub { font-family: "Bebas Neue", sans-serif; color: var(--navy); font-size: 21px; letter-spacing: 2px; text-align: center; line-height: 1; }
  .back-body { margin-top: 42px; font-family: "Arimo", sans-serif; font-size: 11.6px; line-height: 1.33; color: var(--ink); text-align: justify; }
  .back-body p + p { margin-top: 14px; }
  .back-footer { position: absolute; left: 44px; right: 30px; bottom: 58px; display: flex; align-items: center; justify-content: space-between; }
  .company-info { font-style: normal; text-align: center; font-family: "Bebas Neue", sans-serif; color: var(--navy); }
  .company-info .company-name { font-size: 20px; color: var(--teal); }
  .company-info .company-line { font-size: 12px; line-height: 1.2; }

  /* Brand name */
  .brand { display: flex; align-items: center; gap: 6px; font-family: "Bebas Neue", sans-serif; color: var(--navy); line-height: .95; }
  .brand-dot { width: 14px; height: 14px; border-radius: 50%; background: var(--green); flex: none; }
  .brand-name { font-size: 20px; }

  /* Spine */
  .spine {
    position: relative; width: 50px; height: 760px;
    background: linear-gradient(180deg, var(--spine-top), var(--spine-bottom));
    color: #fff; writing-mode: vertical-rl;
    display: flex; align-items: center; padding: 16px 0;
  }
  .spine-kicker { font-family: "Bebas Neue", sans-serif; font-size: 15px; line-height: 1; text-align: center; }
  .spine-kicker span { display: block; font-size: 9px; letter-spacing: 3px; }
  .spine-group { margin-top: 90px; display: flex; align-items: center; gap: 4px; }
  .spine-name { font-family: "Archivo Black", sans-serif; font-size: 26px; line-height: 1; letter-spacing: 1px; }
  .spine-sub { font-family: "Bebas Neue", sans-serif; font-size: 14px; letter-spacing: 2px; line-height: 1; }
  .spine-year { margin-top: auto; font-family: "Bebas Neue", sans-serif; font-size: 34px; line-height: 1; }

  /* Front cover */
  .front { position: relative; width: 430px; height: 760px; background: var(--paper); overflow: hidden; }
  .front-decoration {
    position: absolute; left: 0; top: 0; width: 430px; height: 420px;
    background: linear-gradient(135deg, rgba(122,182,72,.16) 0%, rgba(168,51,107,.14) 40%, rgba(255,194,14,.16) 70%, rgba(255,255,255,0) 100%);
    clip-path: polygon(0 0, 100% 0, 100% 55%, 0 100%);
  }
  .front .brand { position: absolute; left: 18px; top: 46px; }
  .front-illustration {
    position: absolute; left: 38px; top: 178px; width: 208px; height: 180px; border-radius: 12px;
    background: linear-gradient(135deg, #e9f4f2 0%, #bfe6e0 45%, #f8d79a 100%);
  }
  .front-year { position: absolute; right: 44px; top: 360px; font-family: "Bebas Neue", sans-serif; font-size: 100px; line-height: 1; color: var(--navy); }
  .front-title { position: absolute; right: 44px; top: 450px; text-align: right; font-family: "Bebas Neue", sans-serif; font-weight: 400; color: var(--teal); }
  .front-title .title-main { font-size: 64px; line-height: .85; }
  .front-title .title-sub { font-size: 26px; letter-spacing: 6px; line-height: 1; margin-right: -6px; margin-top: 4px; }
  .front-district { position: absolute; left: 0; right: 0; top: 606px; text-align: center; color: var(--navy); font-weight: 400; }
  .front-district .district-name { font-family: "Bebas Neue", sans-serif; font-size: 104px; line-height: .9; }
  .front-district .district-sub { font-family: "Bebas Neue", sans-serif; font-size: 32px; letter-spacing: 2px; line-height: 1; }
</style>
</head>
<body>
<main class="wrap">

  <section class="back">
    <h2 class="back-kicker">Comprehensive Needs Assessment</h2>
    <h1 class="back-district">FAIRMERE</h1>
    <p class="back-district-sub">School District</p>
    <div class="back-body">
      <p>Lorem ipsum dolor sit amet, consectetur adipiscing elit, sed do eiusmod tempor incididunt ut labore et dolore magna aliqua. Magna sit amet purus gravida quis. Mollis nunc sed id semper risus. Amet tellus cras adipiscing enim eu turpis egestas. In nulla posuere sollicitudin aliquam. Purus non enim praesent elementum facilisis leo. Tristique et egestas quis ipsum suspendisse ultrices gravida dictum fusce. At ultrices mi tempus imperdiet nulla malesuada pellentesque elit eget. Ipsum faucibus vitae aliquet nec ullamcorper sit amet risus nullam. Morbi quis commodo odio aenean sed adipiscing diam. Cras fermentum odio eu feugiat pretium nibh ipsum consequat. Id faucibus nisl tincidunt eget nullam. Elit duis tristique sollicitudin nibh sit amet commodo nulla facilisi. Ut pharetra sit amet aliquam id diam maecenas ultricies mi. Turpis in eu mi bibendum neque egestas.</p>
      <p>Nunc non blandit massa enim nec dui nunc mattis enim. Hendrerit gravida rutrum quisque non tellus orci ac auctor. Egestas pretium aenean pharetra magna ac. Luctus accumsan tortor posuere ac ut consequat semper viverra. Tempor orci eu lobortis elementum nibh tellus. Morbi enim nunc faucibus a pellentesque sit amet porttitor eget. Vitae et leo duis ut. Auctor elit sed vulputate mi sit amet mauris. Diam quam nulla porttitor massa id neque aliquam vestibulum morbi. Tortor pretium viverra suspendisse potenti nullam ac. Dapibus ultrices in iaculis nunc sed. Donec ultrices tincidunt arcu non sodales neque sodales. Vitae tortor condimentum lacinia quis vel eros donec ac odio. Amet nulla facilisi morbi tempus. Nulla aliquet porttitor lacus luctus. Consectetur lorem donec massa sapien.</p>
    </div>
    <footer class="back-footer">
      <div class="brand"><span class="brand-dot"></span><span class="brand-name">Learnwell<br>Partners</span></div>
      <address class="company-info">
        <div class="company-name">Learnwell Partners, LLC</div>
        <div class="company-line">4120 Maple Hollow Lane</div>
        <div class="company-line">Riverton, MS 38000</div>
        <div class="company-line">555.210.4480</div>
      </address>
    </footer>
  </section>

  <section class="spine">
    <div class="spine-kicker">Comprehensive<span>Needs Assessment</span></div>
    <div class="spine-group">
      <span class="spine-name">FAIRMERE</span>
      <span class="spine-sub">School District</span>
    </div>
    <div class="spine-year">2023</div>
  </section>

  <section class="front">
    <div class="front-decoration" role="img" aria-label="Decorative diagonal stripes in green, teal, magenta, orange and yellow"></div>
    <div class="brand"><span class="brand-dot"></span><span class="brand-name">Learnwell<br>Partners</span></div>
    <div class="front-illustration" role="img" aria-label="Illustration of a rising market chart, bar graph, receipts and coins with a percent sign"></div>
    <div class="front-year">2023</div>
    <h2 class="front-title"><div class="title-main">COMPREHENSIVE</div><div class="title-sub">NEEDS ASSESSMENT</div></h2>
    <h1 class="front-district"><div class="district-name">FAIRMERE</div><div class="district-sub">SCHOOL DISTRICT</div></h1>
  </section>

</main>
</body>
</html>
```